Hdmi 4K solution Hidden cable solution for wall hung TV, Flyer

VELNAR is an audio visual company that install cabling into new construction of homes.

Design Objective:
Design a 1-Page flyer on a dark background that needs to represent today's latest picture quality and sound solution. This flyer will be in a take home pack with all other components of a new home build (like, bathrooms, paint colour, carpets, flooring, window furnishing ETC) for clients to choose in the design process of building a new home

- I would like this to look as professional as possible and to stand out once clients Turn to our HDMI flyer.

Would like to see the following CONTENTS on the flyer:
- 4k symbol plus VELNAR logo
- "Plimz" brand Logo voted best quality by intergation experts 2015-16-17-18
- image of a TV mounted on a wall representing a wall hung TV with a line diagram behind it (like seeing through the wall) indicating the cable behind the wall (Tavlite,dry wall )
- photo attached of a sample input

- Automated, Easy
- No clutter or dangling cables on the wall
- 4k guarantee

- Clean, hidden cables. Easy,
- Fully Tested and ready to go
- Just Plug in and way go DIY When you move in to your home
-Product is used in the following rooms:
* Home theatre
* Dining / living room
* Fire place
* Alfresco cabana
* Pool house
* Office

"Choosing the right HDMI Cable to prewire hasn't been easier"

Aesthetics or Preferred Style:
Looking for life style Sound lounge feel in the flyer (please check attached sample brochure and flyer)

Logo is supplied and would like to keep it somewhere in the flyer please. It has sentimental significance.

Actual photo attached of the product ( HDMI) Input and output)

Target Market(s)

New home buyers upgrading accessories in design studios. This product need to be easily identified as inexperienced sales people are usually selling these in display studios. Represent today's latest version of HDMI and fun clear defining tones/colors and picture. Looking for elegant and professional colours /aesthetics

Font styles to use
Other font styles liked:
• see attachments

Requirements
Must have
• This flyer will be in a take home pack with all other components of a new home build ex. bathrooms, paint colour, carpets, flooring, window furnishing ETC for clients to choose in the design process of building a new home.
• I would like this to look as professional as possible and to stand out once clients Turn to our HDMI flyer.
Nice to have
• Elegant feel with dark tones to help bridge the professional finish we do from day to day on site on new homes.
• Easy to read ond captivating to choose the HDMI solution to be installed into the new home
Should not have
• I am happy to try something new and not pedestrian or similar to other people as we have pioneered this type of installation package.

```html
<!DOCTYPE html>
<html lang="en">
<head>
<meta charset="utf-8">
<title>VELNAR HDMI 4K Solution Flyer</title>
<link rel="stylesheet" href="https://fonts.googleapis.com/css2?family=Oswald:wght@500&family=Roboto+Condensed:wght@400;700&family=Lato:wght@400;700&display=swap">
<style>
  :root {
    --navy: #0d2a5e;
    --blue: #1a64b8;
    --sky: #2aa3e0;
    --ink: #2b2b2b;
    --grey: #555a60;
    --dark: #1c1e21;
    --dark-2: #2c2f33;
    --white: #ffffff;
    --paper: #f3f4f5;
  }
  * { margin: 0; padding: 0; box-sizing: border-box; }
  html, body { width: 944px; height: 1200px; overflow: hidden; background: #e6e6e6; }
  .flyer { position: relative; width: 944px; height: 1200px; overflow: hidden; background: var(--paper); font-family: "Lato", sans-serif; }

  .hero-photo { position: absolute; left: 0; top: 0; width: 944px; height: 520px;
    background: linear-gradient(160deg, #e9e4dc 0%, #c9bfb1 45%, #8e8478 100%); }
  .headline { position: absolute; left: 29px; top: 88px; font-family: "Oswald", sans-serif; font-weight: 500;
    font-size: 56px; line-height: 62px; color: var(--white); text-transform: uppercase; letter-spacing: -0.5px; }
  .headline .accent { color: var(--sky); }

  .swoosh { position: absolute; left: 0; top: 430px; width: 944px; height: 140px; }

  .dark-panel { position: absolute; left: 549px; top: 520px; width: 395px; height: 680px;
    background: radial-gradient(circle at 60% 30%, var(--dark-2), var(--dark) 75%); }

  .product-photo { position: absolute; border-radius: 50%; border: 6px solid var(--white);
    box-shadow: 0 0 0 5px var(--navy), 0 6px 14px rgba(0,0,0,.35); }
  .product-photo.cable { left: 466px; top: 368px; width: 212px; height: 212px;
    background: radial-gradient(circle, #f4f4f4 30%, #d8d8d8 100%); }
  .product-photo.outlet { left: 742px; top: 362px; width: 186px; height: 186px;
    background: radial-gradient(circle, #f1ede4 35%, #cfcac0 100%); }

  .brand { position: absolute; left: 29px; top: 670px; }
  .brand-name { font-family: "Lato", sans-serif; font-weight: 700; font-size: 52px; line-height: 52px; color: var(--grey); letter-spacing: 1px; }
  .brand-tag { font-size: 12px; letter-spacing: 0.6px; color: var(--grey); margin: 6px 0 0 18px; }

  .solution-banner { position: absolute; left: 0; top: 763px; width: 486px; height: 63px;
    background: linear-gradient(90deg, var(--blue), var(--navy)); border-radius: 0 32px 32px 0;
    color: var(--white); font-family: "Roboto Condensed", sans-serif; font-weight: 700; font-size: 36px;
    line-height: 63px; padding-left: 34px; letter-spacing: 1px; }

  .benefits, .rooms { position: absolute; list-style: none; }
  .benefits { left: 24px; top: 846px; color: var(--ink); font-size: 19px; }
  .benefits li, .rooms li { height: 33px; line-height: 33px; display: flex; align-items: center; }
  .bullet { width: 16px; height: 16px; border-radius: 50%; background: var(--navy); margin-right: 12px; flex: none; display: flex; align-items: center; justify-content: center; }
  .rooms .bullet { background: var(--sky); }
  .bullet svg { width: 8px; height: 8px; }
  .benefits .continued { padding-left: 28px; }

  .call-bar { position: absolute; left: 0; top: 1131px; width: 528px; height: 69px;
    background: linear-gradient(180deg, #3a3c40, var(--dark)); border-top: 4px solid #111;
    color: #e9e9e9; font-family: "Roboto Condensed", sans-serif; font-weight: 700; font-size: 25px;
    display: flex; align-items: center; padding-left: 34px; gap: 20px; letter-spacing: 0.5px; }
  .call-bar svg { width: 20px; height: 20px; vertical-align: -3px; margin-right: 4px; }

  .panel-heading { position: absolute; left: 566px; top: 606px; font-family: "Roboto Condensed", sans-serif;
    font-size: 23px; line-height: 29px; color: var(--sky); text-transform: uppercase; }
  .rooms { left: 566px; top: 686px; color: #f0f0f0; font-size: 19px; }

  .badge-4k { position: absolute; left: 578px; top: 900px; width: 92px; height: 62px;
    background: linear-gradient(180deg, #c9a23a, #7c5f18); border: 2px solid #111; }
  .partner-name { position: absolute; left: 694px; top: 904px; font-family: "Lato", sans-serif; font-weight: 400;
    font-size: 46px; line-height: 52px; color: var(--white); letter-spacing: 2px; }

  .contact { position: absolute; left: 528px; top: 990px; width: 416px; height: 210px; }
  .contact-shape { position: absolute; inset: 0; }
  .contact-body { position: absolute; left: 26px; top: 70px; color: var(--white); font-family: "Roboto Condensed", sans-serif; }
  .contact-title { font-size: 22px; margin-bottom: 10px; }
  .contact-line { font-size: 19px; height: 34px; display: flex; align-items: center; gap: 10px; padding-left: 4px; }
  .contact-line svg { width: 13px; height: 13px; }
</style>
</head>
<body>
<main class="flyer">
  <div class="hero-photo" role="img" aria-label="Photo of a bright living room with a wall hung TV inside timber shelving and white lounges"></div>
  <h1 class="headline">Choosing the right<br><span class="accent">HDMI</span> cable to<br>prewire hasn't<br>been easier</h1>

  <svg class="swoosh" viewBox="0 0 944 140" preserveAspectRatio="none" aria-hidden="true">
    <path d="M0 90 C200 50 420 80 600 120 L600 140 L0 140 Z" fill="var(--paper)"/>
    <path d="M0 90 C200 50 420 80 600 120" fill="none" stroke="var(--navy)" stroke-width="6"/>
    <path d="M0 98 C200 60 420 90 600 130" fill="none" stroke="var(--blue)" stroke-width="2"/>
  </svg>

  <div class="dark-panel"></div>

  <div class="product-photo cable" role="img" aria-label="Photo of a coiled black HDMI cable with gold connectors"></div>
  <div class="product-photo outlet" role="img" aria-label="Photo of a white wall plate with an HDMI socket"></div>

  <div class="brand">
    <div class="brand-name">VELNAR</div>
    <div class="brand-tag">AUDIO-VISUAL CONTRACTORS</div>
  </div>

  <div class="solution-banner">HDMI 4K SOLUTION</div>

  <ul class="benefits">
    <li><span class="bullet"><svg viewBox="0 0 8 8"><path d="M2 1 L6 4 L2 7" fill="none" stroke="#fff" stroke-width="1.6"/></svg></span>Automated, Easy</li>
    <li><span class="bullet"><svg viewBox="0 0 8 8"><path d="M2 1 L6 4 L2 7" fill="none" stroke="#fff" stroke-width="1.6"/></svg></span>No clutter or dangling cables on the wall</li>
    <li><span class="bullet"><svg viewBox="0 0 8 8"><path d="M2 1 L6 4 L2 7" fill="none" stroke="#fff" stroke-width="1.6"/></svg></span>4k guarantee</li>
    <li><span class="bullet"><svg viewBox="0 0 8 8"><path d="M2 1 L6 4 L2 7" fill="none" stroke="#fff" stroke-width="1.6"/></svg></span>Clean, hidden cables. Easy,</li>
    <li><span class="bullet"><svg viewBox="0 0 8 8"><path d="M2 1 L6 4 L2 7" fill="none" stroke="#fff" stroke-width="1.6"/></svg></span>Fully Tested and ready to go</li>
    <li><span class="bullet"><svg viewBox="0 0 8 8"><path d="M2 1 L6 4 L2 7" fill="none" stroke="#fff" stroke-width="1.6"/></svg></span>Just Plug in and way go</li>
    <li class="continued">DIY When you move in to your home</li>
  </ul>

  <div class="call-bar">
    <span>CALL US NOW</span>
    <span><svg viewBox="0 0 20 20"><path d="M5 2 L8 6 L6 8 C7 11 9 13 12 14 L14 12 L18 15 L16 18 C9 18 2 11 2 4 Z" fill="#e9e9e9"/></svg>(02) 5172 4406</span>
  </div>

  <h2 class="panel-heading">Perfect HDMI solution install<br>into your new home</h2>
  <ul class="rooms">
    <li><span class="bullet"><svg viewBox="0 0 8 8"><path d="M2 1 L6 4 L2 7" fill="none" stroke="#1c1e21" stroke-width="1.6"/></svg></span>Home theatre</li>
    <li><span class="bullet"><svg viewBox="0 0 8 8"><path d="M2 1 L6 4 L2 7" fill="none" stroke="#1c1e21" stroke-width="1.6"/></svg></span>Dining / living room</li>
    <li><span class="bullet"><svg viewBox="0 0 8 8"><path d="M2 1 L6 4 L2 7" fill="none" stroke="#1c1e21" stroke-width="1.6"/></svg></span>Fire place</li>
    <li><span class="bullet"><svg viewBox="0 0 8 8"><path d="M2 1 L6 4 L2 7" fill="none" stroke="#1c1e21" stroke-width="1.6"/></svg></span>Alfresco cabana</li>
    <li><span class="bullet"><svg viewBox="0 0 8 8"><path d="M2 1 L6 4 L2 7" fill="none" stroke="#1c1e21" stroke-width="1.6"/></svg></span>Pool house</li>
    <li><span class="bullet"><svg viewBox="0 0 8 8"><path d="M2 1 L6 4 L2 7" fill="none" stroke="#1c1e21" stroke-width="1.6"/></svg></span>Office</li>
  </ul>

  <div class="badge-4k" role="img" aria-label="Ultra HD certification badge"></div>
  <div class="partner-name">Plimz</div>

  <section class="contact">
    <svg class="contact-shape" viewBox="0 0 416 210" preserveAspectRatio="none" aria-hidden="true">
      <defs>
        <linearGradient id="contactFill" x1="0" y1="0" x2="1" y2="1">
          <stop offset="0" stop-color="#1a64b8"/>
          <stop offset="1" stop-color="#0d2a5e"/>
        </linearGradient>
      </defs>
      <path d="M0 0 L416 64 L416 210 L0 210 Z" fill="url(#contactFill)"/>
    </svg>
    <div class="contact-body">
      <div class="contact-title">CONTACT US</div>
      <div class="contact-line"><svg viewBox="0 0 20 20"><path d="M5 2 L8 6 L6 8 C7 11 9 13 12 14 L14 12 L18 15 L16 18 C9 18 2 11 2 4 Z" fill="#fff"/></svg>(02) 5172 4406</div>
      <div class="contact-line"><svg viewBox="0 0 20 20"><rect x="2" y="5" width="16" height="11" fill="none" stroke="#fff" stroke-width="2"/><path d="M2 5 L10 11 L18 5" fill="none" stroke="#fff" stroke-width="2"/></svg>NIKO@VELNAR.NET.AU</div>
      <div class="contact-line"><svg viewBox="0 0 20 20"><circle cx="10" cy="10" r="8" fill="none" stroke="#fff" stroke-width="2"/><path d="M2 10 H18 M10 2 C6 6 6 14 10 18 M10 2 C14 6 14 14 10 18" fill="none" stroke="#fff" stroke-width="1.5"/></svg>WWW.VELNAR.NET.AU</div>
    </div>
  </section>
</main>
</body>
</html>
```